Green Energy Conservation Business Cards

We believe in Conserve before you produce energy. I am looking for a unique, bold business card. that Demonstrates Expertise in our field. I would be interested to try and incorporate a night picture of the US or world showing the yellow lights on one side. I would be open to a design that caters to half the business card size height and same length. Our primary expertise is Energy projects for self storage. Use either black or white background .Attached are the logos and symbols.

May I see some design utilizing a smaller business card. the same length as a normal business card but cut in half on the height. best regards Garrick

```html
<!DOCTYPE html>
<html lang="en">
<head>
<meta charset="utf-8">
<title>Lumeo Energy Group – Business Cards</title>
<link href="https://fonts.googleapis.com/css2?family=Montserrat:wght@500;600&family=Open+Sans:wght@400;600&display=swap" rel="stylesheet">
<style>
  :root {
    --stage: #e7e8ea;
    --card: #ffffff;
    --brand-blue: #1b6fb5;
    --brand-green: #8cc63f;
    --brand-green-light: #c4e26a;
    --ink: #4a4f55;
    --ink-soft: #6d737a;
    --white: #ffffff;
  }
  * { box-sizing: border-box; margin: 0; padding: 0; }
  html, body {
    width: 1200px; height: 899px; overflow: hidden;
    background: var(--stage);
  }
  .stage { position: relative; width: 1200px; height: 899px; }

  .card {
    position: absolute; left: 290px; width: 620px; height: 354px;
    background: var(--card);
    border-radius: 30px;
    overflow: hidden;
    box-shadow: 0 6px 18px rgba(0,0,0,0.12);
  }
  .card--front { top: 70px; }
  .card--back { top: 475px; }

  .front-band { position: absolute; left: 0; top: 0; width: 620px; height: 354px; }

  .holder {
    position: absolute; left: 40px; top: 40px; color: var(--white);
    font-family: "Montserrat", sans-serif; text-transform: uppercase;
  }
  .holder-name { font-size: 24px; font-weight: 500; letter-spacing: 0.5px; line-height: 30px; }
  .holder-title { font-size: 13px; font-weight: 500; letter-spacing: 1px; line-height: 18px; }

  .address {
    position: absolute; left: 40px; top: 160px;
    font-family: "Open Sans", sans-serif; font-size: 12px; line-height: 17px;
    color: var(--ink);
  }
  .contacts {
    position: absolute; left: 40px; top: 214px; list-style: none;
    font-family: "Open Sans", sans-serif; font-size: 10.5px; color: var(--ink-soft);
  }
  .contacts li { display: flex; align-items: center; height: 19px; white-space: nowrap; }
  .contacts svg { width: 11px; height: 11px; margin-right: 9px; fill: var(--brand-blue); flex: none; }

  .brand {
    position: absolute; display: flex; align-items: center;
    font-family: "Montserrat", sans-serif; font-weight: 600; color: var(--brand-blue);
    white-space: nowrap;
  }
  .brand-dot { border-radius: 50%; background: var(--brand-green); flex: none; }
  .brand-name { line-height: 1.1; }

  .card--front .brand { left: 340px; top: 206px; }
  .card--front .brand-dot { width: 44px; height: 44px; margin-right: 12px; }
  .card--front .brand-name { font-size: 22px; }

  .card--back .brand { left: 50%; top: 50%; transform: translate(-50%, -50%); }
  .card--back .brand-dot { width: 56px; height: 56px; margin-right: 16px; }
  .card--back .brand-name { font-size: 28px; }
</style>
</head>
<body>
<main class="stage">

  <section class="card card--front" aria-label="Business card front">
    <svg class="front-band" viewBox="0 0 620 354" aria-hidden="true">
      <path d="M0 0 H620 V78 C470 92 300 128 0 128 Z" fill="var(--brand-blue)"/>
      <path d="M0 128 C300 128 470 92 620 78 V84 C470 100 300 136 0 136 Z" fill="var(--brand-green-light)"/>
      <path d="M0 133 C300 133 470 100 620 88" fill="none" stroke="var(--brand-green)" stroke-width="3"/>
      <path d="M60 142 C320 140 480 108 620 96" fill="none" stroke="var(--brand-green-light)" stroke-width="1.5"/>
    </svg>

    <div class="holder">
      <p class="holder-name">Dustin Garrick</p>
      <p class="holder-title">Financial Advisor</p>
    </div>

    <p class="address">214 9th Floor Hall<br>Meadow Road UKG</p>

    <ul class="contacts">
      <li><svg viewBox="0 0 12 12"><path d="M2.5 1 L4.5 1 L5.3 3.5 L4 4.6 C4.6 6 5.8 7.3 7.3 8 L8.4 6.7 L11 7.5 V9.5 C11 10.4 10.3 11 9.5 11 C5 11 1 7 1 2.5 C1 1.7 1.7 1 2.5 1 Z"/></svg>021 555 0148</li>
      <li><svg viewBox="0 0 12 12"><path d="M3.5 0.5 H8.5 A1 1 0 0 1 9.5 1.5 V10.5 A1 1 0 0 1 8.5 11.5 H3.5 A1 1 0 0 1 2.5 10.5 V1.5 A1 1 0 0 1 3.5 0.5 Z M3.7 2 V9 H8.3 V2 Z"/></svg>021 555 0149</li>
      <li><svg viewBox="0 0 12 12"><path d="M3 0.5 H9 V4 H3 Z M1 4.5 H11 V9.5 H9 V11.5 H3 V9.5 H1 Z M4 8 V10.5 H8 V8 Z"/></svg>021 555 0150</li>
      <li><svg viewBox="0 0 12 12"><path d="M0.5 2.5 H11.5 V9.5 H0.5 Z M1.5 3.3 L6 6.6 L10.5 3.3 Z" fill-rule="evenodd"/></svg>info@lumeoenergy.com</li>
      <li><svg viewBox="0 0 12 12"><path d="M6 0.5 A5.5 5.5 0 1 0 6 11.5 A5.5 5.5 0 1 0 6 0.5 Z M6 1.8 A4.2 4.2 0 1 1 6 10.2 A4.2 4.2 0 1 1 6 1.8 Z M1.5 5.4 H10.5 V6.6 H1.5 Z M5.4 1.5 H6.6 V10.5 H5.4 Z"/></svg>www.lumeoenergy.com</li>
    </ul>

    <div class="brand">
      <span class="brand-dot"></span>
      <span class="brand-name">Lumeo<br>Energy Group</span>
    </div>
  </section>

  <section class="card card--back" aria-label="Business card back">
    <div class="brand">
      <span class="brand-dot"></span>
      <span class="brand-name">Lumeo<br>Energy Group</span>
    </div>
  </section>

</main>
</body>
</html>
```